Banner Ad Design Project for Home Technology Company

We need banner ads designed for our company. See the description of what we do below the basic messages listed, section titled "ABOUT TALLWICKET"

Basic Messages:
See it. Hear it. Live it.

1. Message #1: Discover YOUR Tallwicket. Audio? Video? Media Rooms? Connected Home? We do it all!

2. Message #2: Audio
You don't need magical ears to find the perfect speakers. It's as simple as: "Which speakers sound best to you?" We can help, but it's ultimately your decision.

3. Message #3: Digital Media
- Option A: The future of how we listen to music is happening now.
- Option B: Are you just listening to your music or are you enjoying it?
- Option C: Take control of your music.
- Option D: If you aren't blown away, we aren't doing our job!

4. Message #4: Media Room
It doesn't matter where you want to watch TV & movies, enjoy your favorite music, or host parties where your guests get to be the DJ, we can help you create your ultimate entertainment zone. We've created numerous media rooms, dedicated home theaters, game rooms, and whole home entertainment systems.

5. Message #5: Connected Home
Enhance your home and your life.

ABOUT TALLWICKET:
Technology is everywhere. It’s hard to imagine any aspect of our lives that doesn’t involve it. From phones to our cars, from work to our home, technology enhances our lives, bringing us closer to information, entertainment, and each other. Often though, our different devices exist in isolation, connecting us to the world, but rarely working together to create a more elegant whole. It doesn’t have to be that way.

Imagine a home that greets you by unlocking the front door, disabling the security system, turning on lights, and welcoming you with your favorite music. Imagine a home that automatically lowers shades before the sun can fade your furniture and décor. Imagine a favorite song playing in each room of the house, or the latest hit film streaming and displayed across a wall-sized screen. Imagine prompting all of this from your smart phone.

This is only the beginning of the promise offered by an intelligent home. Beyond showcasing the latest technology, the ultimate goal is to make interaction with your home’s advanced automation features a pleasure. Exceptionally easy, yet wonderfully sophisticated, it is technology designed to help you manage your life.It’s about living in the home of the future, right now.

Here at Tallwicket we’ve helped families make complex technology simple for over 36 years. We provide advanced, professional, creative resources dedicated to ensuring your project’s success. From beautifully integrated design to the finest home technologies, we’ll guide you through each step of the design and installation process to make certain you have exactly the products you need, the features you want, and the personal attention that will make the home of the future a joy to own today.

Enhance your home and your life; let us show you how.
Updates

Brief will be completed soon. Please wait until that has been posted.  I'm setting up projects now, then adding the creative briefs.

Thank you for your patience.

Brief has been updated & Lots of information has been added.

Project Deadline Extended

Added a file with some lifestyle photos of products we sell. If you need others, please make a request.

Some lifestyle product photos of products we sell can be downloaded from this link: http://shrt.example/Xq7r

We are still looking for more designs. While we've found a few that we do like, we're still looking for more.  That's why we've extended the deadline by another week.  Please continue to submit designs as all will be considered.

Target Market(s)

English-speaking adults, aged 35-55. 60% are married; 40% have children in the household. 75% have college degrees or greater. These are innovation seekers, design & technology enthusiasts. They're interested in having premium experiences, top brands, being the first to own the latest and greatest in technology.

Industry/Entity Type

Entertainment

Requirements
Must have
- Must include only one message per banner ad set.
- Must mimic the current design style of tallwicket.example.
- Please make sure that each individual banners file size is less than 40k
Nice to have
• Button that allows viewers to click through to our website. Button should include text such as:
- Learn More
- Discover More

The above are purely examples; other calls-to-action could also work.
Should not have
• Curved Lines.

```html
<!DOCTYPE html>
<html lang="en">
<head>
<meta charset="utf-8">
<title>Tallwicket Banner Set</title>
<link rel="stylesheet" href="https://fonts.googleapis.com/css2?family=Alegreya+Sans:wght@400;500;700&display=swap">
<style>
  :root {
    --backdrop: #3d2a1e;
    --brand-yellow: #fbb829;
    --header-white: #ffffff;
    --ink: #111111;
    --band-dark: #1d1d1d;
    --button-top: #5a5a5a;
    --button-bottom: #111111;
    --button-text: #ffffff;
    --accent-orange: #f7a21b;
    --horn-light: #e4e4e4;
    --horn-mid: #9a9a9a;
    --cabinet-brown: #4a2c1a;
  }
  * { margin: 0; padding: 0; box-sizing: border-box; }
  html, body { width: 1200px; height: 761px; overflow: hidden; background: var(--backdrop); }
  body { font-family: "Alegreya Sans", sans-serif; color: var(--ink); }

  .stage { position: absolute; left: 0; top: 0; width: 1076px; height: 682px; transform: scale(1.1152); transform-origin: 0 0; }

  .banner { position: absolute; background: var(--brand-yellow); overflow: hidden; }
  .banner > * { position: absolute; }
  .banner-shape { left: 0; top: 0; width: 100%; height: 100%; }

  .brand { display: flex; align-items: center; gap: 5px; font-weight: 500; letter-spacing: 0.02em; white-space: nowrap; }
  .brand-dot { display: inline-block; border-radius: 50%; background: var(--accent-orange); }
  .tagline { font-weight: 400; white-space: nowrap; }

  .headline { font-weight: 500; line-height: 1.15; white-space: nowrap; }
  .questions { font-weight: 400; line-height: 1.3; }
  .closer { font-weight: 700; white-space: nowrap; }

  .cta {
    display: flex; align-items: center; justify-content: center;
    background: linear-gradient(var(--button-top), var(--button-bottom));
    color: var(--button-text); border-radius: 3px; font-weight: 500;
    box-shadow: 0 2px 3px rgba(0,0,0,0.35); white-space: nowrap;
  }

  .gramophone-art {
    background:
      radial-gradient(ellipse at 70% 30%, var(--horn-light) 0%, var(--horn-mid) 35%, transparent 60%),
      linear-gradient(to bottom, transparent 55%, var(--cabinet-brown) 56%, #2a180d 100%);
    border-radius: 6px;
  }

  /* Skyscraper 160x600 */
  .skyscraper { left: 126px; top: 22px; width: 160px; height: 600px; }
  .skyscraper .brand { left: 8px; top: 88px; font-size: 19px; }
  .skyscraper .brand-dot { width: 10px; height: 10px; }
  .skyscraper .tagline { left: 10px; top: 124px; font-size: 15px; }
  .skyscraper .headline { left: 0; width: 160px; top: 168px; text-align: center; font-size: 22px; }
  .skyscraper .headline span { font-size: 25px; }
  .skyscraper .questions { left: 0; width: 160px; top: 238px; text-align: center; font-size: 19px; line-height: 25.5px; }
  .skyscraper .closer { left: 0; width: 160px; top: 372px; text-align: center; font-size: 24px; }
  .skyscraper .gramophone-art { left: 16px; top: 405px; width: 134px; height: 170px; }
  .skyscraper .cta { left: 16px; top: 563px; width: 124px; height: 27px; font-size: 16px; }

  /* Medium rectangle 336x280 */
  .rect-large { left: 328px; top: 59px; width: 336px; height: 280px; }
  .rect-large .brand { left: 7px; top: 58px; font-size: 17px; }
  .rect-large .brand-dot { width: 9px; height: 9px; }
  .rect-large .tagline { left: 11px; top: 88px; font-size: 13px; }
  .rect-large .headline { left: 11px; top: 125px; font-size: 25px; }
  .rect-large .headline span { font-size: 27px; }
  .rect-large .questions { left: 10px; top: 200px; font-size: 16px; line-height: 23px; }
  .rect-large .closer { left: 11px; top: 248px; font-size: 21px; }
  .rect-large .gramophone-art { left: 192px; top: 0; width: 144px; height: 185px; }
  .rect-large .cta { left: 197px; top: 239px; width: 124px; height: 28px; font-size: 16px; }

  /* Medium rectangle 300x250 */
  .rect-medium { left: 689px; top: 72px; width: 300px; height: 250px; }
  .rect-medium .brand { left: 7px; top: 50px; font-size: 15px; }
  .rect-medium .brand-dot { width: 8px; height: 8px; }
  .rect-medium .tagline { left: 9px; top: 77px; font-size: 12px; }
  .rect-medium .headline { left: 9px; top: 112px; font-size: 22px; }
  .rect-medium .headline span { font-size: 24px; }
  .rect-medium .questions { left: 9px; top: 180px; font-size: 14.5px; line-height: 20px; }
  .rect-medium .closer { left: 9px; top: 223px; font-size: 19px; }
  .rect-medium .gramophone-art { left: 148px; top: 0; width: 152px; height: 172px; }
  .rect-medium .cta { left: 176px; top: 214px; width: 110px; height: 24px; font-size: 14px; }

  /* Banner 468x60 */
  .banner-wide { left: 371px; top: 444px; width: 468px; height: 58px; }
  .banner-wide .brand { left: 4px; top: 30px; font-size: 9.5px; }
  .banner-wide .brand-dot { width: 6px; height: 6px; }
  .banner-wide .tagline { left: 5px; top: 44px; font-size: 7.5px; }
  .banner-wide .headline { left: 110px; top: 6px; font-size: 14px; }
  .banner-wide .questions { left: 110px; width: 204px; top: 24px; text-align: center; font-size: 12px; line-height: 14.5px; }
  .banner-wide .gramophone-art { left: 306px; top: 2px; width: 64px; height: 55px; }
  .banner-wide .closer { left: 373px; top: 8px; font-size: 14px; }
  .banner-wide .cta { left: 374px; top: 29px; width: 80px; height: 18px; font-size: 10px; }

  /* Leaderboard 728x90 */
  .leaderboard { left: 300px; top: 532px; width: 728px; height: 90px; }
  .leaderboard .brand { left: 6px; top: 48px; font-size: 15px; }
  .leaderboard .brand-dot { width: 8px; height: 8px; }
  .leaderboard .tagline { left: 10px; top: 73px; font-size: 11.5px; }
  .leaderboard .headline { left: 171px; top: 8px; font-size: 24px; }
  .leaderboard .questions { left: 170px; width: 298px; top: 38px; text-align: center; font-size: 18.5px; line-height: 24px; }
  .leaderboard .gramophone-art { left: 472px; top: 2px; width: 86px; height: 86px; }
  .leaderboard .closer { left: 580px; top: 13px; font-size: 23px; }
  .leaderboard .cta { left: 583px; top: 45px; width: 124px; height: 28px; font-size: 16px; }
</style>
</head>
<body>
<main class="stage">

  <section class="banner skyscraper" aria-label="Tallwicket banner 160 by 600">
    <svg class="banner-shape" viewBox="0 0 160 600" aria-hidden="true">
      <path d="M0 0 H160 V144 C120 152 70 142 0 152 Z" fill="var(--header-white)"/>
      <path d="M0 153 C70 143 120 153 160 145" fill="none" stroke="var(--band-dark)" stroke-width="7"/>
    </svg>
    <div class="brand"><span class="brand-dot"></span>TALLWICKET</div>
    <p class="tagline">See it. Hear it. Live it.</p>
    <h2 class="headline">Discover YOUR<br><span>Tallwicket</span></h2>
    <p class="questions">Audio?<br>Video?<br>Media Rooms?<br>Connected<br>Home?</p>
    <p class="closer">We do it all!</p>
    <div class="gramophone-art" role="img" aria-label="Antique gramophone with silver horn on a wooden cabinet"></div>
    <a class="cta">Learn More!</a>
  </section>

  <section class="banner rect-large" aria-label="Tallwicket banner 336 by 280">
    <svg class="banner-shape" viewBox="0 0 336 280" aria-hidden="true">
      <path d="M0 0 H200 V96 C150 104 80 118 0 110 Z" fill="var(--header-white)"/>
      <path d="M0 112 C80 120 150 106 230 98" fill="none" stroke="var(--band-dark)" stroke-width="5"/>
    </svg>
    <div class="brand"><span class="brand-dot"></span>TALLWICKET</div>
    <p class="tagline">See it. Hear it. Live it.</p>
    <div class="gramophone-art" role="img" aria-label="Antique gramophone with silver horn on a wooden cabinet"></div>
    <h2 class="headline">Discover YOUR<br><span>Tallwicket</span></h2>
    <p class="questions">Audio? Video? Media Rooms?<br>Connected Home?</p>
    <p class="closer">We do it all!</p>
    <a class="cta">Learn More!</a>
  </section>

  <section class="banner rect-medium" aria-label="Tallwicket banner 300 by 250">
    <svg class="banner-shape" viewBox="0 0 300 250" aria-hidden="true">
      <path d="M0 0 H160 V86 C120 92 60 104 0 98 Z" fill="var(--header-white)"/>
      <path d="M0 100 C60 106 130 94 190 88" fill="none" stroke="var(--band-dark)" stroke-width="4"/>
    </svg>
    <div class="brand"><span class="brand-dot"></span>TALLWICKET</div>
    <p class="tagline">See it. Hear it. Live it.</p>
    <div class="gramophone-art" role="img" aria-label="Antique gramophone with silver horn on a wooden cabinet"></div>
    <h2 class="headline">Discover YOUR<br><span>Tallwicket</span></h2>
    <p class="questions">Audio? Video? Media Rooms?<br>Connected Home?</p>
    <p class="closer">We do it all!</p>
    <a class="cta">Learn More!</a>
  </section>

  <section class="banner banner-wide" aria-label="Tallwicket banner 468 by 60">
    <svg class="banner-shape" viewBox="0 0 468 58" aria-hidden="true">
      <path d="M0 0 H94 C102 20 102 40 94 58 H0 Z" fill="var(--header-white)"/>
      <path d="M95 0 C103 20 103 40 95 58" fill="none" stroke="var(--band-dark)" stroke-width="4"/>
    </svg>
    <div class="brand"><span class="brand-dot"></span>TALLWICKET</div>
    <p class="tagline">See it. Hear it. Live it.</p>
    <h2 class="headline">Discover YOUR Tallwicket</h2>
    <p class="questions">Audio? Video? Media Rooms?<br>Connected Home?</p>
    <div class="gramophone-art" role="img" aria-label="Antique gramophone with silver horn on a wooden cabinet"></div>
    <p class="closer">We do it all!</p>
    <a class="cta">Learn More!</a>
  </section>

  <section class="banner leaderboard" aria-label="Tallwicket banner 728 by 90">
    <svg class="banner-shape" viewBox="0 0 728 90" aria-hidden="true">
      <path d="M0 0 H146 C158 30 158 60 146 90 H0 Z" fill="var(--header-white)"/>
      <path d="M148 0 C160 30 160 60 148 90" fill="none" stroke="var(--band-dark)" stroke-width="6"/>
    </svg>
    <div class="brand"><span class="brand-dot"></span>TALLWICKET</div>
    <p class="tagline">See it. Hear it. Live it.</p>
    <h2 class="headline">Discover YOUR Tallwicket</h2>
    <p class="questions">Audio? Video? Media Rooms?<br>Connected Home?</p>
    <div class="gramophone-art" role="img" aria-label="Antique gramophone with silver horn on a wooden cabinet"></div>
    <p class="closer">We do it all!</p>
    <a class="cta">Learn More!</a>
  </section>

</main>
</body>
</html>
```